Design a Home Page UI using photoshop or Adobe XD

- Need a Ui design for real estate company . This is a home page design with different sections as mentioned below.
Home page has :
- Navigation Bar ( Logo and links to other pages )
- Heroic Image ( with a message Helping people to find their Dream Home )
- Statistics( This section is to mention how many houses sold , how many projects , how many Happy customers )
- About us ( Brief text about company and link to about us page )
- Map
- Footer
Logo is attached and a sample paper wire frame for reference ( It is just for reference you can design conveying the whole theme )
- If you are using stock free images please provide us links for attribution (If your entry is selected )

```html
<!DOCTYPE html>
<html lang="en">
<head>
<meta charset="utf-8">
<title>Varuna Homes – Home</title>
<link rel="stylesheet" href="https://fonts.googleapis.com/css2?family=Montserrat:wght@500;600;700&family=Open+Sans:wght@300;400;600;700&display=swap">
<style>
:root{
  --blue:#1478d4;
  --blue-dark:#0f66b8;
  --ink:#1d1d1d;
  --grey-text:#6b6b6b;
  --footer:#555555;
  --white:#ffffff;
  --hero-a:#3b3550;
  --hero-b:#6a4a3a;
  --hero-c:#2a2a3a;
}
*{margin:0;padding:0;box-sizing:border-box}
html,body{width:1200px;height:3612px;overflow:hidden;background:var(--white)}
body{position:relative;font-family:"Open Sans",sans-serif;color:var(--ink)}
.abs{position:absolute}

/* top bar */
.topbar{left:0;top:0;width:1200px;height:69px;background:var(--blue)}
.topbar .phone{left:100px;top:20px;width:30px;height:30px}
.topbar .phone-text{left:154px;top:23px;font-size:17px;color:var(--white)}
.social{top:26px;width:18px;height:18px;border-radius:50%;background:var(--white)}

/* nav */
.brand{left:98px;top:104px;display:flex;align-items:center;gap:12px}
.brand-mark{width:40px;height:58px;background:var(--blue)}
.brand-name{font-family:"Montserrat",sans-serif;font-weight:700;font-size:26px;color:var(--blue);letter-spacing:1px}
.nav-link{top:114px;font-family:"Montserrat",sans-serif;font-weight:600;font-size:19px;letter-spacing:2.5px;color:var(--grey-text)}
.nav-link.active{color:#333}
.nav-underline{left:556px;top:148px;width:70px;height:3px;background:var(--blue)}

/* hero */
.hero{left:0;top:198px;width:1200px;height:615px;background:linear-gradient(180deg,var(--hero-a) 0%,var(--hero-b) 55%,var(--hero-c) 100%)}
.hero-title{left:188px;font-family:"Montserrat",sans-serif;font-weight:700;font-size:50px;letter-spacing:4px;color:var(--white);line-height:1}
.btn{display:flex;align-items:center;justify-content:center;gap:22px;background:var(--blue);color:var(--white);border-radius:9px;font-family:"Montserrat",sans-serif;font-weight:500;font-size:22px;letter-spacing:2px}
.hero-btn{left:186px;top:627px;width:247px;height:70px}
.hero-arrow{top:468px;width:40px;height:64px}
.dot{top:735px;width:20px;height:20px;border-radius:50%;background:rgba(255,255,255,.45)}
.dot.on{background:var(--white)}

/* section headings */
.heading{width:400px;text-align:center;font-family:"Montserrat",sans-serif;font-weight:500;font-size:29px;letter-spacing:3px;color:var(--ink)}
.rule{height:3px;background:var(--blue)}

/* about */
.about-photo{left:45px;top:997px;width:573px;height:381px;background:linear-gradient(135deg,#c9a878 0%,#5b4a3a 45%,#2f3b3e 100%);box-shadow:20px 20px 18px rgba(0,0,0,.22)}
.about-text{left:678px;top:990px;width:480px;text-align:center;font-size:27px;font-weight:300;letter-spacing:1.8px;line-height:49.3px;color:#222}
.about-btn{left:774px;top:1367px;width:247px;height:70px;box-shadow:6px 8px 12px rgba(0,0,0,.2)}

/* stats */
.band{left:0;top:1490px}
.stat{width:240px;text-align:center;color:var(--white);font-size:24px;letter-spacing:3px;line-height:38px}

/* contact */
.label{left:53px;font-size:27px;letter-spacing:2px;color:#222}
.field{left:53px;width:414px;border:1.5px solid #777;background:var(--white)}
.send{left:171px;top:2864px;width:177px;height:60px;border-radius:4px;background:var(--blue);color:var(--white);font-family:"Montserrat",sans-serif;font-size:27px;letter-spacing:3px;display:flex;align-items:center;justify-content:center}
.map{left:547px;top:2362px;width:614px;height:501px;background:linear-gradient(135deg,#eef0f2 0%,#e2e5e8 50%,#f1efe8 100%)}

/* footer */
.footer{left:0;top:3163px;width:1200px;height:449px;background:var(--footer)}
.f-head{width:240px;text-align:center;font-size:19px;letter-spacing:2.5px;color:var(--white)}
.f-rule{height:1.5px;background:var(--white)}
.f-about{left:54px;top:3330px;width:320px;text-align:center;font-size:18.5px;letter-spacing:1.5px;line-height:39.3px;color:#eee}
.f-link{width:240px;text-align:center;font-size:20px;font-weight:700;letter-spacing:2.5px;color:var(--white)}
.f-item{left:851px;font-size:19px;letter-spacing:2.5px;color:#eee}
.f-icon{left:810px;width:28px;height:28px}
</style>
</head>
<body>

<header>
  <div class="abs topbar">
    <svg class="abs phone" viewBox="0 0 24 24"><path fill="#fff" d="M6.6 10.8a15.1 15.1 0 0 0 6.6 6.6l2.2-2.2c.3-.3.7-.4 1-.2 1.1.4 2.3.6 3.6.6.6 0 1 .4 1 1V20c0 .6-.4 1-1 1A17 17 0 0 1 3 4c0-.6.4-1 1-1h3.5c.6 0 1 .4 1 1 0 1.3.2 2.5.6 3.6.1.3 0 .7-.2 1z"/></svg>
    <div class="abs phone-text">+91 9000012345</div>
    <span class="abs social" style="left:960px"></span>
    <span class="abs social" style="left:1012px"></span>
    <span class="abs social" style="left:1070px"></span>
  </div>

  <nav>
    <div class="abs brand"><span class="brand-mark"></span><span class="brand-name">VARUNA HOMES</span></div>
    <span class="abs nav-link active" style="left:556px">HOME</span>
    <span class="abs nav-underline"></span>
    <span class="abs nav-link" style="left:664px">ABOUT US</span>
    <span class="abs nav-link" style="left:829px">PROJECTS</span>
    <span class="abs nav-link" style="left:988px">CONTACT</span>
  </nav>
</header>

<section class="hero-section">
  <div class="abs hero" role="img" aria-label="Modern two-storey house lit at dusk beside a pool"></div>
  <h1>
    <span class="abs hero-title" style="top:390px">Helping People To</span>
    <span class="abs hero-title" style="top:483px">Find Their Dream Home</span>
  </h1>
  <div class="abs btn hero-btn">Learn More
    <svg width="26" height="26" viewBox="0 0 24 24"><path d="M3 12h17M13 4l8 8-8 8" fill="none" stroke="#fff" stroke-width="3" stroke-linecap="round" stroke-linejoin="round"/></svg>
  </div>
  <svg class="abs hero-arrow" style="left:42px" viewBox="0 0 40 64"><path d="M32 4 6 32l26 28" fill="none" stroke="#fff" stroke-width="5" stroke-linecap="round"/></svg>
  <svg class="abs hero-arrow" style="left:1134px" viewBox="0 0 40 64"><path d="M8 4l26 28L8 60" fill="none" stroke="#fff" stroke-width="5" stroke-linecap="round"/></svg>
  <span class="abs dot on" style="left:531px"></span>
  <span class="abs dot" style="left:587px"></span>
  <span class="abs dot" style="left:643px"></span>
</section>

<section class="about">
  <h2 class="abs heading" style="left:407px;top:879px">ABOUT US</h2>
  <span class="abs rule" style="left:521px;top:930px;width:174px"></span>
  <span class="abs rule" style="left:531px;top:941px;width:153px;height:2px"></span>
  <div class="abs about-photo" role="img" aria-label="Wooden house among trees at sunrise"></div>
  <p class="abs about-text">Lorem ipsum dolor sit amet, consectetur adipiscing elit. Quisque hendrerit feugiat sem. Class aptent taciti sociosqu ad litora torquent per conubia nostra,per inceptos himenaeos. Fusce asem sit amet.</p>
  <div class="abs btn about-btn">Learn More
    <svg width="26" height="26" viewBox="0 0 24 24"><path d="M3 12h17M13 4l8 8-8 8" fill="none" stroke="#fff" stroke-width="3" stroke-linecap="round" stroke-linejoin="round"/></svg>
  </div>
</section>

<section class="stats">
  <svg class="abs band" width="1200" height="680" viewBox="0 0 1200 680">
    <path fill="var(--blue)" d="M0 193 L1130 14 Q1180 6 1200 0 L1200 501 L0 669 Z"/>
  </svg>
  <!-- key in hand -->
  <svg class="abs" style="left:178px;top:1720px" width="110" height="106" viewBox="0 0 110 106">
    <g fill="none" stroke="#fff" stroke-width="4" stroke-linecap="round" stroke-linejoin="round">
      <circle cx="82" cy="22" r="15"/><circle cx="82" cy="22" r="5"/>
      <path d="M71 33 45 60M52 53l7 7M58 47l6 6"/>
      <path d="M4 78h16v26H4zM20 82c10-6 22-8 32-4h18c6 0 6 8 0 8H52M20 100c20 2 40-2 60-16l18-12c5-3 1-10-5-7L70 78"/>
    </g>
  </svg>
  <!-- house with tick -->
  <svg class="abs" style="left:579px;top:1742px" width="94" height="86" viewBox="0 0 94 86">
    <path fill="#fff" d="M34 4 2 34h10v40h22V54h14v20h10V34h10z"/>
    <path d="M50 56l12 12 24-26" fill="none" stroke="#3cbf5a" stroke-width="9" stroke-linecap="round" stroke-linejoin="round"/>
  </svg>
  <!-- smile -->
  <svg class="abs" style="left:954px;top:1738px" width="68" height="68" viewBox="0 0 68 68">
    <circle cx="34" cy="34" r="33" fill="#fff"/>
    <g fill="none" stroke="var(--blue)" stroke-width="4" stroke-linecap="round">
      <path d="M18 28q5-6 10 0M40 28q5-6 10 0M18 40q16 16 32 0"/>
    </g>
  </svg>
  <div class="abs stat" style="left:111px;top:1839px">330+<br><span style="line-height:54px">Houses</span><br><span style="position:relative;top:-16px">Sold</span></div>
  <div class="abs stat" style="left:504px;top:1839px">38+<br><span style="line-height:54px">Projects</span></div>
  <div class="abs stat" style="left:868px;top:1832px">1221+<br><span style="line-height:56px">Happy</span><br><span style="position:relative;top:-16px">Clients</span></div>
</section>

<section class="contact">
  <h2 class="abs heading" style="left:396px;top:2206px">CONTACT US</h2>
  <span class="abs rule" style="left:491px;top:2257px;width:213px"></span>
  <span class="abs rule" style="left:514px;top:2268px;width:170px;height:2px"></span>

  <span class="abs label" style="top:2344px">Your Name</span>
  <span class="abs field" style="top:2396px;height:59px"></span>
  <span class="abs label" style="top:2481px;left:56px">Your Email</span>
  <span class="abs field" style="top:2532px;height:59px"></span>
  <span class="abs label" style="top:2617px;left:56px">Your Message</span>
  <span class="abs field" style="top:2668px;height:151px"></span>
  <div class="abs send">SEND</div>

  <div class="abs map" role="img" aria-label="Street map showing the office location with a red pin"></div>
</section>

<footer>
  <div class="abs footer"></div>
  <h3 class="abs f-head" style="left:94px;top:3233px">ABOUT US</h3>
  <span class="abs f-rule" style="left:141px;top:3271px;width:150px"></span>
  <span class="abs f-rule" style="left:151px;top:3278px;width:126px"></span>
  <p class="abs f-about">Lorem ipsum dolor sit amet, consectetur adipiscing elit. Quisque hendrerit feugiat sem. Class aptent taciti sociosqu</p>

  <h3 class="abs f-head" style="left:474px;top:3223px">QUICK LINKS</h3>
  <span class="abs f-rule" style="left:518px;top:3261px;width:150px"></span>
  <span class="abs f-rule" style="left:528px;top:3268px;width:126px"></span>
  <span class="abs f-link" style="left:473px;top:3330px">HOME</span>
  <span class="abs f-link" style="left:476px;top:3379px">ABOUT US</span>
  <span class="abs f-link" style="left:476px;top:3428px">PROJECTS</span>
  <span class="abs f-link" style="left:476px;top:3480px">CONTACT</span>

  <h3 class="abs f-head" style="left:868px;top:3233px">CONTACT US</h3>
  <span class="abs f-rule" style="left:918px;top:3271px;width:150px"></span>
  <span class="abs f-rule" style="left:928px;top:3278px;width:126px"></span>

  <svg class="abs f-icon" style="top:3334px" viewBox="0 0 24 24"><path fill="#fff" d="M12 2a7 7 0 0 0-7 7c0 5 7 13 7 13s7-8 7-13a7 7 0 0 0-7-7zm0 9.5A2.5 2.5 0 1 1 12 6.5a2.5 2.5 0 0 1 0 5z"/></svg>
  <span class="abs f-item" style="top:3334px">Street No-546,Town,Country</span>
  <svg class="abs f-icon" style="top:3396px;left:814px" viewBox="0 0 24 24"><path fill="#fff" d="M6.6 10.8a15.1 15.1 0 0 0 6.6 6.6l2.2-2.2c.3-.3.7-.4 1-.2 1.1.4 2.3.6 3.6.6.6 0 1 .4 1 1V20c0 .6-.4 1-1 1A17 17 0 0 1 3 4c0-.6.4-1 1-1h3.5c.6 0 1 .4 1 1 0 1.3.2 2.5.6 3.6.1.3 0 .7-.2 1z"/></svg>
  <span class="abs f-item" style="top:3397px;left:862px">+91 9000012345</span>
  <svg class="abs f-icon" style="top:3461px;left:808px;width:34px" viewBox="0 0 24 18"><path fill="#fff" d="M1 1h22v16H1z"/><path d="M1.5 1.5 12 10l10.5-8.5" fill="none" stroke="var(--footer)" stroke-width="1.8"/></svg>
  <span class="abs f-item" style="top:3461px;left:865px">yourmail@name.com</span>
</footer>

</body>
</html>
```